Bully breed rescue website

I need a website for my bully breed rescue. We rescue bully breeds from up and down the east coast of the United States and train them as service dogs for people with limited mobility disabilities. I don't want a lot of white space. I want it to be modern and slick and colorful and still look professional. I want it to be different and have a lot of wow factor. I linked a copy of my logo.

Number of Pages Required

5+ page

Font styles to use
Sans Serif

Colors

Designer to choose colors to be used in the design.

Requirements
Must have
• Moving aspects. Blog and ecommerce.
• 1.) Home page
• 2.) Services- something modular
• 3.) About US
• 4.) Blog
• 5.) Application page
• 6.) Donation page
• 7.) Contact Us
Nice to have
• Large Slider of photos on home page
• vertical menu bar
Should not have
• Lots of white space. Dont want it to look like a template or any other site

```html
<!DOCTYPE html>
<html lang="en">
<head>
<meta charset="utf-8">
<title>Gentle Jaws Rescue</title>
<link href="https://fonts.googleapis.com/css2?family=Poppins:wght@400;500;600;700&family=Teko:wght@400;500&display=swap" rel="stylesheet">
<style>
:root{
  --red:#c8101a;
  --red-bright:#e8232c;
  --peach:#fcc98c;
  --cream:#f3ece6;
  --sand:#dcc9bd;
  --brown:#6b452a;
  --brown-dark:#4d3020;
  --ochre:#e2a53a;
  --rust:#8a4d22;
  --teal:#2ab3c4;
  --pink:#f0556a;
  --cyan:#33bfd6;
  --gold:#f5b13b;
  --ink:#2a2220;
  --footer:#262626;
  --white:#ffffff;
}
*{margin:0;padding:0;box-sizing:border-box}
html,body{width:1200px;height:3758px;overflow:hidden}
body{font-family:"Poppins",sans-serif;color:var(--ink);background:var(--cream);position:relative}
.abs{position:absolute}
.ph{position:absolute}
p{line-height:1.6}

/* header / hero */
.hero{left:0;top:0;width:1200px;height:600px;background:linear-gradient(160deg,#a99c86 0%,#7f725f 45%,#5b4f40 100%)}
.brand{left:214px;top:8px;display:flex;align-items:center;gap:10px;z-index:3}
.brand-dot{width:46px;height:46px;border-radius:50%;background:var(--white)}
.brand-name{font-weight:700;font-size:17px;color:var(--white)}
.nav{left:478px;top:55px;width:500px;height:34px;background:var(--brown);display:flex;justify-content:space-around;align-items:center;z-index:3}
.nav a{color:var(--white);font-size:11px;font-weight:600;text-decoration:none;text-transform:uppercase}
.donate-btn{left:880px;top:0;width:135px;height:46px;background:var(--red-bright);color:var(--white);font-size:12px;font-weight:600;display:flex;align-items:center;justify-content:center;clip-path:polygon(8% 0,100% 0,92% 100%,0 100%);z-index:3}
.hero-title{left:560px;top:275px;text-align:center;color:var(--white);font-family:"Teko",sans-serif;line-height:.95}
.hero-title small{display:block;font-size:40px}
.hero-title strong{display:block;font-size:60px;font-weight:500}
.arrow-btn{width:34px;height:34px;border-radius:50%;background:var(--white);display:flex;align-items:center;justify-content:center;top:318px}

/* about */
.red-band{left:0;top:560px;width:1200px;height:250px}
.about-box{left:210px;top:656px;width:312px;height:376px;background:var(--peach);padding:28px 26px}
.about-box h2{font-size:19px;line-height:1.1;font-weight:700;text-transform:uppercase;color:var(--ink)}
.about-box h2 span{display:block;font-size:15px;font-weight:600}
.about-box p{font-size:10px;margin-top:14px;color:#4a3a2e}
.btn-brown{display:inline-block;background:var(--brown);color:var(--white);font-size:9px;padding:9px 20px;font-weight:600;text-transform:uppercase}
.about-photo{left:522px;top:656px;width:468px;height:376px;background:linear-gradient(135deg,#c99a63,#8c9a4c 55%,#4f7a2c)}
.mv{top:1065px;width:370px}
.mv h3{font-size:14px;font-weight:700;text-transform:uppercase}
.mv p{font-size:10px;margin-top:12px;color:#5a4b40}

/* help */
.help{left:0;top:1220px;width:1200px;height:335px;background:var(--sand)}
.help-dog{left:0;top:1250px;width:185px;height:300px;background:linear-gradient(180deg,#e5ddd4,#a38f80);border-radius:0 120px 0 0}
.section-title{font-size:17px;font-weight:700;text-transform:uppercase;text-align:center;width:1200px;left:0}
.card{top:1320px;width:245px;height:191px;color:var(--white);text-align:center;padding-top:20px}
.card .icon{width:60px;height:60px;border-radius:50%;border:2px solid var(--white);margin:0 auto;display:flex;align-items:center;justify-content:center}
.card h4{font-size:15px;font-weight:500;text-transform:uppercase;margin-top:12px}
.card p{font-size:9px;margin:16px 30px 0}
.card-donate{background:linear-gradient(180deg,#3fc4d8,#1aa0c2)}
.card-sponsor{background:linear-gradient(180deg,#f56a7c,#e63c56)}
.card-dire{background:linear-gradient(180deg,#4fd1c3,#1fb3b5)}

/* sponsor band */
.sponsor{left:0;top:1555px;width:1200px;height:175px;background:var(--ochre)}
.sponsor-text{left:240px;top:1610px;color:var(--white);font-size:15px;line-height:1.55;text-align:center}
.sponsor-mail{left:242px;top:1660px;color:var(--white);font-size:15px;display:flex;gap:10px;align-items:center}
.sponsor-photo{left:575px;top:1548px;width:410px;height:185px;background:linear-gradient(135deg,#5d8a2e,#a3b260 60%,#c88e52);transform:skewX(-8deg);border:4px solid var(--brown-dark)}

/* dogs */
.dogs{left:0;top:1730px;width:1200px;height:400px;background:var(--brown)}
.dogs .section-title{color:var(--white);top:1796px}
.dogs-sub{left:0;width:1200px;text-align:center;color:var(--white);font-size:10px;top:1832px;line-height:1.6}
.dog-thumb{top:1898px;width:180px;height:181px;border:3px solid var(--white)}
.slide-arrow{top:1975px}

/* policies */
.policies{left:0;top:2130px;width:1200px;height:352px;background:linear-gradient(90deg,#3d2c22,#6b5648 50%,#a48a70)}
.policy-dog{left:0;top:2195px;width:200px;height:235px;background:linear-gradient(160deg,#c99a63,#7a5536);border-radius:0 40px 40px 0}
.policies .section-title{color:var(--ochre);top:2176px}
.pill{left:473px;top:2220px;width:215px;height:30px;background:#6a5040;color:var(--white);font-size:8px;display:flex;align-items:center;justify-content:center;border-radius:2px}
.policy{top:2285px;width:225px;color:var(--white);text-align:center}
.policy h5{font-size:13px;font-weight:400}
.policy p{font-size:9.5px;margin-top:16px}

/* split rescue */
.split-left{left:0;top:2482px;width:633px;height:445px;background:var(--rust)}
.split-right{left:633px;top:2482px;width:567px;height:445px;background:linear-gradient(135deg,#3a2f2c,#251d1b)}
.rescue-copy{left:208px;top:2528px;width:260px;color:var(--white)}
.rescue-copy h3{font-size:15px;font-weight:700;text-transform:uppercase}
.rescue-copy p{font-size:9px;margin-top:14px}
.rescue-copy a{color:#ffb07a;text-decoration:none}
.tile{left:543px;width:447px;height:107px;color:var(--white);display:flex;align-items:center;padding:0 18px;gap:22px}
.tile .icon{width:54px;height:54px;border-radius:50%;border:2px solid rgba(255,255,255,.8);flex:none;display:flex;align-items:center;justify-content:center}
.tile h6{font-size:12px;font-weight:500}
.tile p{font-size:9px;margin-top:6px}
.tile-teal{top:2525px;background:var(--teal)}
.tile-gold{top:2640px;background:var(--gold)}
.tile-pink{top:2755px;background:var(--pink)}

/* posts */
.posts{left:0;top:2927px;width:1200px;height:550px;background:var(--sand)}
.posts .section-title{top:2972px}
.post{top:3036px;width:232px;height:333px;background:var(--white);box-shadow:0 2px 8px rgba(0,0,0,.12)}
.post .thumb{width:232px;height:135px}
.post .body{padding:14px 16px}
.post .date{font-size:8px;color:#8a7a70}
.post h4{font-size:13px;font-weight:500;line-height:1.3;margin-top:6px}
.post p{font-size:8.5px;color:#6a5a50;margin-top:10px}
.post .more{font-size:8px;color:var(--brown);margin-top:12px;text-transform:uppercase;display:block}
.posts-btn{left:545px;top:3416px}

/* footer */
.footer{left:0;top:3477px;width:1200px;height:281px;background:var(--footer);color:var(--white)}
.footer-nav{left:0;top:3505px;width:1200px;display:flex;justify-content:center;gap:26px;font-size:9px;color:#ddd}
.footer-rule{left:180px;top:3533px;width:840px;height:1px;background:#444}
.f-col{top:3570px;font-size:9px;line-height:1.9;color:#ddd}
.f-col b{display:block;color:var(--white);font-weight:600;margin-bottom:6px}
.f-phone{font-size:19px;color:var(--white);letter-spacing:1px}
.f-brand{left:498px;top:3560px;width:205px;display:flex;flex-direction:column;align-items:center;gap:8px}
.f-brand .brand-dot{width:42px;height:42px}
.f-brand span{font-weight:700;font-size:18px}
.newsletter{left:752px;top:3604px;display:flex}
.newsletter div{width:180px;height:32px;background:var(--white);color:#999;font-size:9px;display:flex;align-items:center;padding-left:12px}
.newsletter b{width:88px;height:32px;background:var(--brown);font-size:10px;font-weight:600;display:flex;align-items:center;justify-content:center}
.social{left:752px;top:3652px;display:flex;gap:12px}
.social i{width:10px;height:10px;background:#ccc;display:block;border-radius:2px}
.copyright{left:0;top:3683px;width:1200px;text-align:center;font-size:9px;color:#bbb}
</style>
</head>
<body>

<!-- header & hero slider -->
<div class="abs hero" role="img" aria-label="Hero slide: photograph of a bulldog sitting in dry grass"></div>
<div class="abs brand"><div class="brand-dot"></div><span class="brand-name">Gentle Jaws Rescue</span></div>
<nav class="abs nav"><a>Home</a><a>Services</a><a>About Us</a><a>Blog</a><a>Application</a><a>Donation</a><a>Contact Us</a></nav>
<div class="abs donate-btn">DONATE</div>
<div class="abs hero-title"><small>Welcome to</small><strong>Gentle Jaws Rescue</strong></div>
<div class="abs arrow-btn" style="left:152px"><svg width="12" height="12" viewBox="0 0 12 12"><path d="M8 1 3 6l5 5" fill="none" stroke="#333" stroke-width="2"/></svg></div>
<div class="abs arrow-btn" style="left:1008px"><svg width="12" height="12" viewBox="0 0 12 12"><path d="M4 1l5 5-5 5" fill="none" stroke="#333" stroke-width="2"/></svg></div>

<!-- about -->
<svg class="abs red-band" viewBox="0 0 1200 250" preserveAspectRatio="none">
  <path d="M0 40 Q300 10 600 25 T1200 20 V250 H0Z" fill="#f3ece6"/>
  <path d="M0 40 Q300 10 600 25 T1200 20 V200 H0Z" fill="#c8101a"/>
</svg>
<div class="abs about-box">
  <h2><span>About</span>Gentle Jaws Rescue</h2>
  <p>Lorem ipsum dolor sit amet, consectetur adipiscing elit, sed do eiusmod tempor incididunt ut labore et dolore magna aliqua. Ut enim ad minim veniam, quis nostrud exercitation ullamco laboris nisi ut aliquip ex ea commodo consequat. Duis aute irure dolor in reprehenderit in voluptate velit esse cillum dolore eu fugiat nulla pariatur.</p>
  <p>Excepteur sint occaecat cupidatat non proident, sunt in culpa qui officia deserunt mollit anim id est laborum.</p>
  <div class="btn-brown" style="margin-top:20px">Read More</div>
</div>
<div class="abs about-photo" role="img" aria-label="Photograph of a bulldog puppy lying on grass"></div>
<div class="abs mv" style="left:210px"><h3>Our Mission</h3><p>Lorem ipsum dolor sit amet, consectetur adipiscing elit, sed do eiusmod tempor incididunt ut labore et dolore magna aliqua. Ut enim ad minim veniam, quis nostrud exercitation ullamco laboris nisi ut aliquip ex ea commodo consequat.</p></div>
<div class="abs mv" style="left:608px"><h3>Our Vision</h3><p>Lorem ipsum dolor sit amet, consectetur adipiscing elit, sed do eiusmod tempor incididunt ut labore et dolore magna aliqua. Ut enim ad minim veniam, quis nostrud exercitation ullamco laboris nisi ut aliquip ex ea commodo consequat.</p></div>

<!-- how you can help -->
<div class="abs help"></div>
<div class="abs help-dog" role="img" aria-label="Photograph of a white bulldog walking"></div>
<h2 class="abs section-title" style="top:1266px">How You Can Help</h2>
<div class="abs card card-donate" style="left:210px">
  <div class="icon"><svg width="28" height="28" viewBox="0 0 28 28"><circle cx="14" cy="12" r="7" fill="none" stroke="#fff" stroke-width="2"/><path d="M3 24h22" stroke="#fff" stroke-width="2"/></svg></div>
  <h4>Donate</h4><p>Sed ut perspiciatis unde omnis iste natus error sit voluptatem accusantium</p>
</div>
<div class="abs card card-sponsor" style="left:478px">
  <div class="icon"><svg width="28" height="28" viewBox="0 0 28 28"><circle cx="14" cy="15" r="8" fill="none" stroke="#fff" stroke-width="2"/><path d="M6 9 4 4l6 3M22 9l2-5-6 3" fill="none" stroke="#fff" stroke-width="2"/></svg></div>
  <h4>Sponsor a Dog</h4><p>Sed ut perspiciatis unde omnis iste natus error sit voluptatem accusantium</p>
</div>
<div class="abs card card-dire" style="left:746px">
  <div class="icon"><svg width="28" height="28" viewBox="0 0 28 28"><circle cx="14" cy="18" r="5" fill="#fff"/><circle cx="7" cy="11" r="2.5" fill="#fff"/><circle cx="21" cy="11" r="2.5" fill="#fff"/><circle cx="11" cy="6" r="2.5" fill="#fff"/><circle cx="17" cy="6" r="2.5" fill="#fff"/></svg></div>
  <h4>Dire Cases</h4><p>Sed ut perspiciatis unde omnis iste natus error sit voluptatem accusantium</p>
</div>

<!-- sponsor band -->
<div class="abs sponsor"></div>
<div class="abs sponsor-text">If you are interested in becoming a sponsor<br>for Gentle Jaws Rescue please email at:</div>
<div class="abs sponsor-mail" style="top:1660px"><svg width="20" height="16" viewBox="0 0 20 16"><rect x="1" y="1" width="18" height="14" fill="none" stroke="#fff" stroke-width="1.5"/><path d="M1 1l9 7 9-7" fill="none" stroke="#fff" stroke-width="1.5"/></svg>hello@gentlejawsrescue.org</div>
<div class="abs sponsor-photo" role="img" aria-label="Photograph of a bulldog on green grass"></div>

<!-- dogs available -->
<div class="abs dogs"></div>
<h2 class="abs section-title" style="top:1796px;color:#fff">Dogs Available for Foster and/or Adoption</h2>
<div class="abs dogs-sub">In a perfect world, every dog would have a home and every home would have a dog.<br>(Click on photo for more information)</div>
<div class="abs dog-thumb" style="left:210px;background:linear-gradient(135deg,#8fae5a,#c9a77a)" role="img" aria-label="Photograph of a bulldog in grass"></div>
<div class="abs dog-thumb" style="left:408px;background:linear-gradient(135deg,#e6e1da,#c09a70)" role="img" aria-label="Photograph of a bulldog indoors"></div>
<div class="abs dog-thumb" style="left:608px;background:linear-gradient(135deg,#6a6a5a,#2b2420)" role="img" aria-label="Photograph of a dark brindle bulldog"></div>
<div class="abs dog-thumb" style="left:808px;background:linear-gradient(135deg,#d8a35a,#e9e1d6)" role="img" aria-label="Photograph of a white bulldog among autumn leaves"></div>
<svg class="abs slide-arrow" style="left:165px" width="26" height="26" viewBox="0 0 26 26"><path d="M24 13H3M11 5l-8 8 8 8" fill="none" stroke="#fff" stroke-width="2.5"/></svg>
<svg class="abs slide-arrow" style="left:1005px" width="26" height="26" viewBox="0 0 26 26"><path d="M2 13h21M15 5l8 8-8 8" fill="none" stroke="#fff" stroke-width="2.5"/></svg>

<!-- policies -->
<div class="abs policies" role="img" aria-label="Blurred warm background photograph"></div>
<div class="abs policy-dog" role="img" aria-label="Photograph of a bulldog looking toward the camera"></div>
<h2 class="abs section-title" style="top:2176px;color:#e2a53a">Bully Breed Rescue Policies</h2>
<div class="abs pill">FOSTER &amp; ADOPTION POLICY – PLEASE READ FIRST</div>
<div class="abs policy" style="left:218px"><h5>Bully Breed Ambassadors</h5><p>Lorem ipsum dolor sit amet, consectetur adipiscing elit, sed do eiusmod tempor incididunt ut labore et dolore magna aliqua. Ut enim ad minim veniam, quis nostrud exercitation ullamco laboris nisi ut aliquip ex ea commodo consequat.</p></div>
<div class="abs policy" style="left:488px"><h5>For Accepting Shelter Dogs</h5><p>Lorem ipsum dolor sit amet, consectetur adipiscing elit, sed do eiusmod tempor incididunt ut labore et dolore magna aliqua. Ut enim ad minim veniam, quis nostrud exercitation ullamco laboris nisi ut aliquip ex ea commodo consequat.</p></div>
<div class="abs policy" style="left:755px"><h5>Owner Surrender &amp; Strays</h5><p>Lorem ipsum dolor sit amet, consectetur adipiscing elit, sed do eiusmod tempor incididunt ut labore et dolore magna aliqua. Ut enim ad minim veniam, quis nostrud exercitation ullamco laboris nisi ut aliquip ex ea commodo consequat.</p></div>

<!-- rescue split -->
<div class="abs split-left"></div>
<div class="abs split-right" role="img" aria-label="Photograph of a black French bulldog"></div>
<div class="abs rescue-copy">
  <h3>Bully Breed Rescue....</h3>
  <p>Sed ut perspiciatis unde omnis iste natus error sit voluptatem accusantium doloremque laudantium, totam rem aperiam, eaque ipsa quae ab illo inventore veritatis et quasi architecto beatae vitae dicta sunt explicabo. Nemo enim ipsam voluptatem quia voluptas sit aspernatur aut odit aut fugit, sed quia consequuntur magni dolores eos qui ratione voluptatem sequi nesciunt. Neque porro quisquam est, qui dolorem ipsum quia dolor sit amet, consectetur, adipisci velit, sed quia non numquam eius modi tempora incidunt ut labore et dolore magnam aliquam quaerat voluptatem. Ut enim ad minima veniam.</p>
  <p>If you have a rescue inquiry please email <a>rescue@gentlejawsrescue.org</a>. Your email will be forwarded to the appropriate volunteer.</p>
</div>
<div class="abs tile tile-teal"><div class="icon"><svg width="26" height="26" viewBox="0 0 26 26"><circle cx="10" cy="9" r="4" fill="none" stroke="#fff" stroke-width="2"/><path d="M3 22c0-5 14-5 14 0" fill="none" stroke="#fff" stroke-width="2"/><circle cx="18" cy="8" r="3" fill="none" stroke="#fff" stroke-width="1.5"/></svg></div><div><h6>...is a volunteer only organization:</h6><p>Lorem ipsum dolor sit amet, consectetur adipiscing elit, sed do eiusmod tempor incididunt ut labore et dolore magna aliqua.</p></div></div>
<div class="abs tile tile-gold"><div class="icon"><svg width="26" height="26" viewBox="0 0 28 28"><circle cx="14" cy="18" r="5" fill="#fff"/><circle cx="7" cy="11" r="2.5" fill="#fff"/><circle cx="21" cy="11" r="2.5" fill="#fff"/><circle cx="11" cy="6" r="2.5" fill="#fff"/><circle cx="17" cy="6" r="2.5" fill="#fff"/></svg></div><div><h6>... accepts bully breed dogs that have:</h6><p>Lorem ipsum dolor sit amet, consectetur adipiscing elit, sed do eiusmod tempor incididunt ut labore et dolore magna aliqua.</p></div></div>
<div class="abs tile tile-pink"><div class="icon"><svg width="26" height="26" viewBox="0 0 28 28"><circle cx="14" cy="15" r="8" fill="none" stroke="#fff" stroke-width="2"/><path d="M6 9 4 4l6 3M22 9l2-5-6 3" fill="none" stroke="#fff" stroke-width="2"/></svg></div><div><h6>...owner surrender &amp; strays:</h6><p>Lorem ipsum dolor sit amet, consectetur adipiscing elit, sed do eiusmod tempor incididunt ut labore et dolore magna aliqua.</p></div></div>

<!-- recent posts -->
<div class="abs posts"></div>
<h2 class="abs section-title" style="top:2972px">Recent Posts</h2>
<article class="abs post" style="left:210px"><div class="thumb" style="background:linear-gradient(135deg,#9fc06a,#4f7a2c)" role="img" aria-label="Photograph of a bulldog running on grass"></div><div class="body"><div class="date">April 23, 2018</div><h4>Lorem ipsum dolor sit amet, consectetur</h4><p>Sed ut perspiciatis unde omnis iste natus error sit voluptatem accusan tium doloremque laudantium, totam</p><span class="more">Read More</span></div></article>
<article class="abs post" style="left:484px"><div class="thumb" style="background:linear-gradient(135deg,#3a2c26,#a07a5a)" role="img" aria-label="Photograph of a bulldog in a car seat"></div><div class="body"><div class="date">April 23, 2018</div><h4>Lorem ipsum dolor sit amet, consectetur</h4><p>Sed ut perspiciatis unde omnis iste natus error sit voluptatem accusan tium doloremque laudantium, totam</p><span class="more">Read More</span></div></article>
<article class="abs post" style="left:758px"><div class="thumb" style="background:linear-gradient(135deg,#b7d28a,#6a9a3e)" role="img" aria-label="Photograph of a bulldog in a sunny garden"></div><div class="body"><div class="date">April 23, 2018</div><h4>Lorem ipsum dolor sit amet, consectetur</h4><p>Sed ut perspiciatis unde omnis iste natus error sit voluptatem accusan tium doloremque laudantium, totam</p><span class="more">Read More</span></div></article>
<div class="abs btn-brown posts-btn">Read More Blog</div>

<!-- footer -->
<footer class="abs footer"></footer>
<div class="abs footer-nav"><span>Home</span><span>Services</span><span>About US</span><span>Blog</span><span>Application</span><span>Donation</span><span>Contact Us</span></div>
<div class="abs footer-rule"></div>
<div class="abs f-col" style="left:182px"><b>Address</b>Gentle Jaws Rescue<br>Lorem ipsum dolor<br>Adipiscing elit 00000</div>
<div class="abs f-col" style="left:325px"><b>Call Us</b><span class="f-phone">123-456-7890</span></div>
<div class="abs f-brand"><div class="brand-dot"></div><span>Gentle Jaws Rescue</span></div>
<div class="abs f-col" style="left:752px"><b>Sign Up to Our Newsletter</b></div>
<div class="abs newsletter"><div>Your email address</div><b>SIGN UP</b></div>
<div class="abs social"><i></i><i></i><i></i></div>
<div class="abs copyright">©2018 Gentle Jaws Rescue. All Rights Reserved. &nbsp; Privacy Policy</div>

</body>
</html>
```